依頼詳細
大分県内では最大のシェアを確保していますが、最近では同業他社も増え始め、弊社のチラシと酷似しているチラシも見かけるようになりました。そこで、新キャラクターを作成してもらいました。工場の新設をきっかけに、新キャラクターを前面に押し出し、同業他社と一見して区別してもらえるような、インパクトが強く、イメージに残るようなチラシを募集したいと考えています。弊社(そよかぜ本舗)のチラシ、他社のチラシも添付しています。現在のチラシとイメージが一新してもかまいません。

要望
・キャラクターは添付の新キャラクター「ねむぽん」を使用してください。
・「工場新設キャンペーン」を実施します。実施期間は未定な為、「○月○日~○月○日」という表記でお願い致します。また当キャンペーン中は「ふとん3枚で9000円」です。
・新工場の写真も載せたいので、工事前の工場の写真(添付ファイル)を入れてください。新工場が完成した後差し替えます。
・住所欄には「大分市みなと坂町24-8(旧住所)」と「大分市霞台506-9(新住所)」の記載

よろしくお願い致します。
記載項目
屋号/社名/住所/フリーダイヤル/電話番号/営業時間/URL/料金プラン/なんでもふとん3枚で9000円+税/電話一本集配無料/丸洗い中の貸布団無料/来客用貸布団/工場新設キャンペーンについて
サイズ
A5
ページ数
両面
希望イメージ
シンプル 複雑
単色 カラフル
暗い 明るい
日常 高級
遊び心 厳粛
未来的 伝統的
女性的 男性的
希望する色
納品ファイル
• 高解像度JPG (.jpg)
• イラストレーター形式 (.ai)
• フォトショップ形式 (.psd)
補足説明
工場写真の添付。
要望の追加です。
キャラクターが新しくなった事を伝えたいので、「ねむぽくん(旧キャラクター)」から「ねむぽん(新キャラクター)」へ変わったということを、両キャラクターを使用して入れてください。
■ 選んだ理由

新しいというイメージと色使いが他社との差別化ができるとおもい、選びました。

■ 提案者全員のお礼・コメント

すばらしい提案ばかりですごく悩みました。GW前のお忙しい中、おとり組いただきありがとうございました。
また別件でもお仕事をお願いする予定ですので、今後とも宜しくお願いします。
本当にありがとうございました。

```html
<!DOCTYPE html>
<html lang="ja">
<head>
<meta charset="utf-8">
<title>ふとん丸洗い 工場新設記念キャンペーン｜そよかぜ本舗</title>
<link href="https://fonts.googleapis.com/css2?family=M+PLUS+Rounded+1c:wght@500;700;800;900&family=Noto+Sans+JP:wght@500;700;900&display=swap" rel="stylesheet">
<style>
:root{
  --mint:#e2f4e8;
  --mint-deep:#bfe6cc;
  --blue:#1f6fc6;
  --blue-dark:#184f95;
  --navy:#1d2f6b;
  --red:#e2231a;
  --yellow:#ffe600;
  --orange:#f4a23c;
  --green:#3a9a3c;
  --white:#ffffff;
  --ink:#222;
}
*{margin:0;padding:0;box-sizing:border-box}
html,body{width:842px;height:1200px;overflow:hidden;background:#fff}
.flyer{
  position:relative;width:842px;height:1200px;overflow:hidden;
  background:radial-gradient(circle at 70% 30%, #fff 0, var(--mint) 45%, var(--mint-deep) 100%);
  font-family:"M PLUS Rounded 1c","Noto Sans JP",sans-serif;color:var(--navy);
}
.abs{position:absolute}
.campaign-ribbon{
  left:26px;top:40px;width:540px;height:68px;background:var(--white);
  transform:rotate(-5deg);border-radius:8px;box-shadow:0 4px 0 var(--green);
  display:flex;align-items:center;justify-content:center;white-space:nowrap;
  font-weight:900;font-size:34px;color:var(--green);letter-spacing:1px;
}
.factory-photo{
  left:575px;top:14px;width:250px;height:118px;border:5px solid var(--white);
  background:linear-gradient(180deg,#b9c9d6 0%,#e6eaee 55%,#8a969f 100%);
}
.title-band{
  left:40px;top:160px;width:765px;height:132px;background:var(--blue);
  border-radius:24px;box-shadow:0 6px 0 var(--blue-dark);
  display:flex;align-items:center;justify-content:center;gap:10px;
  font-weight:900;font-size:100px;color:var(--white);letter-spacing:2px;white-space:nowrap;
}
.title-band .maru{
  display:inline-flex;align-items:center;justify-content:center;
  width:160px;height:160px;margin-top:-10px;border-radius:50%;background:var(--white);
  color:var(--red);font-size:130px;box-shadow:0 5px 0 var(--blue-dark);
}
.any-size{
  left:165px;top:304px;width:640px;height:46px;background:var(--red);
  display:flex;align-items:center;justify-content:center;white-space:nowrap;
  font-weight:900;font-size:32px;color:var(--yellow);letter-spacing:2px;
}
.any-size-note{left:165px;top:356px;width:660px;font-size:16px;font-weight:700;white-space:nowrap}
.cards-art{left:26px;top:400px;width:118px;height:100px;border-radius:10px;
  background:linear-gradient(135deg,var(--orange),#f7c170)}
.deal-lead{left:160px;top:398px;font-size:28px;font-weight:900;white-space:nowrap}
.deal-count{left:156px;top:436px;font-size:86px;font-weight:900;color:var(--red);line-height:1;white-space:nowrap}
.deal-count small{font-size:50px}
.price-box{
  left:385px;top:396px;width:428px;height:102px;background:var(--yellow);border-radius:12px;
  display:flex;align-items:flex-end;justify-content:center;padding-bottom:4px;white-space:nowrap;
  font-weight:900;color:var(--red);font-size:96px;line-height:1;
}
.price-box .yen{font-size:58px;margin-bottom:8px}
.price-box .tax{font-size:18px;color:var(--navy);margin:0 0 12px 4px}
.mascot-art{
  left:300px;top:600px;width:520px;height:560px;border-radius:46% 46% 30% 30%;
  background:radial-gradient(circle at 50% 40%,#ef4b3f 0,var(--red) 60%,#b71a14 100%);
}
.rental-free{
  left:490px;top:530px;width:330px;height:62px;background:var(--white);border-radius:31px;
  transform:rotate(-4deg);display:flex;align-items:center;justify-content:center;white-space:nowrap;
  font-weight:900;font-size:27px;color:var(--navy);
}
.pickup-badge{
  left:20px;top:540px;width:260px;height:260px;border-radius:50%;background:var(--red);
  border:6px solid var(--white);
  display:flex;flex-direction:column;align-items:center;justify-content:center;gap:4px;text-align:center;
  color:var(--white);font-weight:900;
}
.pickup-badge .lead{font-size:28px}
.pickup-badge .area{background:var(--white);color:var(--navy);font-size:14px;padding:2px 10px;border-radius:10px;white-space:nowrap}
.pickup-badge .free{font-size:48px;color:var(--yellow);line-height:1.05}
.pickup-badge .hours{font-size:13px;line-height:1.3;font-weight:700;white-space:nowrap}
.shop-info{left:24px;top:872px;width:340px}
.shop-type{background:var(--green);color:var(--white);font-weight:800;font-size:22px;text-align:center;padding:4px 0;border-radius:8px 8px 0 0}
.shop-name{background:var(--white);color:var(--navy);font-weight:900;font-size:40px;text-align:center;padding:2px 0;border:3px solid var(--green);border-radius:0 0 8px 8px;white-space:nowrap}
.tel-row{display:flex;align-items:center;gap:8px;margin-top:6px;font-weight:900;color:var(--navy);white-space:nowrap}
.tel-free{font-size:34px;line-height:1.1}
.tel-local{font-size:26px;line-height:1.1}
.tel-row svg{flex:none}
.details{margin-top:6px;font-size:13px;line-height:1.45;font-weight:700;color:var(--ink);white-space:nowrap}
.mascot-caption{left:650px;top:1170px;font-size:13px;font-weight:700;color:var(--navy);white-space:nowrap}
</style>
</head>
<body>
<main class="flyer">
  <div class="abs campaign-ribbon">祝！工場新設記念キャンペーン</div>
  <div class="abs factory-photo" role="img" aria-label="新工場の写真"></div>

  <h1 class="abs title-band">ふとん<span class="maru">丸</span>洗い</h1>
  <p class="abs any-size">サイズ・種類問わず！なんでも！</p>
  <p class="abs any-size-note">綿ふとん・羊毛ふとん・羽毛ふとん・こたつ布団 ※じゅうたん類は含まれません</p>

  <div class="abs cards-art" role="img" aria-label="重ねたふとんのイラスト"></div>
  <p class="abs deal-lead">まとめてお得！</p>
  <p class="abs deal-count">3<small>枚で</small></p>
  <p class="abs price-box">9,000<span class="yen">円</span><span class="tax">(税抜)</span></p>

  <div class="abs mascot-art" role="img" aria-label="新キャラクター「ねむぽん」のイラスト"></div>
  <p class="abs rental-free">貸し布団も無料で安心♪</p>

  <div class="abs pickup-badge">
    <span class="lead">お電話一本</span>
    <span class="area">大分市・別府市・挾間町</span>
    <span class="free">集配<br>無料</span>
    <span class="hours">夜8時まで電話受付<br>翌日朝までに集配OK!</span>
  </div>

  <section class="abs shop-info">
    <p class="shop-type">ふとん丸洗い専門店</p>
    <p class="shop-name">そよかぜ本舗</p>
    <div class="tel-row">
      <svg width="34" height="24" viewBox="0 0 34 24"><circle cx="9" cy="12" r="8" fill="none" stroke="#1d2f6b" stroke-width="4"/><circle cx="25" cy="12" r="8" fill="none" stroke="#1d2f6b" stroke-width="4"/></svg>
      <span class="tel-free">0120-318-726</span>
    </div>
    <div class="tel-row">
      <svg width="24" height="24" viewBox="0 0 24 24"><path fill="#1d2f6b" d="M6.6 10.8a15 15 0 0 0 6.6 6.6l2.2-2.2a1 1 0 0 1 1-.25 11.4 11.4 0 0 0 3.6.57 1 1 0 0 1 1 1V20a1 1 0 0 1-1 1A17 17 0 0 1 3 4a1 1 0 0 1 1-1h3.5a1 1 0 0 1 1 1c0 1.25.2 2.45.57 3.57a1 1 0 0 1-.25 1z"/></svg>
      <span class="tel-local">097-540-2893</span>
    </div>
    <p class="details">
      【電話受付】AM10:00〜PM9:00<br>
      【集配】AM10:00〜PM6:00【定休日】日祭日<br>
      【旧住所】大分市みなと坂町24-8<br>
      【新住所】大分市霞台506-9
    </p>
  </section>

  <p class="abs mascot-caption">新キャラクター／ねむぽん</p>
</main>
</body>
</html>
```